TRVA Banner

This is for a generic retractable banner to be used anytime our group goes to large conferences and meetings. Please do not use any of the pictures from our website or reference Chicago or any of the events are attending. The plan is to use this banner anytime we go to a conference, set up at career fairs and have a table at a meeting.
We are the Crossward Surgical Results Alliance (TRVA) and I have included our logo. The website is: www.trva-net.org
Below are some qualities about our group, but please do not use these as a bullet point list on the banner. These are an overview of what we do at TRVA:
- Anesthesiologists / Anesthesiology
- Research, Quality and Education
- Large data repository
- Quality Champions
- Medical Researchers
- Perioperative Outcomes
- Innovators and trailblazers
- Medical research

```html
<!DOCTYPE html>
<html lang="en">
<head>
<meta charset="utf-8">
<title>TRVA Retractable Banner</title>
<link rel="stylesheet" href="https://fonts.googleapis.com/css2?family=Montserrat:wght@600;700;800&family=Roboto+Condensed:wght@400&family=Oswald:wght@400;500&display=swap">
<style>
  :root{
    --navy:#163f73;
    --blue:#1b73ba;
    --blue-light:#2d9be0;
    --green:#7ab42a;
    --orange:#f28a1c;
    --orange-dark:#d8730e;
    --white:#ffffff;
    --stage:#eceded;
  }
  *{box-sizing:border-box;margin:0;padding:0}
  html,body{width:1200px;height:1000px;overflow:hidden}
  body{background:var(--stage);font-family:"Montserrat",sans-serif;position:relative}

  .banner{position:absolute;left:400px;top:20px;width:400px;height:960px;background:var(--white);overflow:hidden;box-shadow:0 4px 18px rgba(0,0,0,.12)}

  .brand{position:absolute;top:44px;left:0;width:100%;display:flex;align-items:center;justify-content:center;gap:12px}
  .brand-mark{width:34px;height:34px;border-radius:50%;background:var(--green);flex:none}
  .brand-text{display:flex;flex-direction:column;color:var(--navy);font-weight:700}
  .brand-name{font-size:42px;line-height:1;letter-spacing:1px}
  .brand-full{margin-top:6px;font-size:12.5px;line-height:1.2}

  .headline{position:absolute;top:172px;width:100%;text-align:center;font-weight:800;font-size:25px;line-height:1.14;color:var(--navy)}
  .headline .accent-green{color:var(--green)}
  .headline .accent-blue{color:var(--blue)}

  .mission{position:absolute;top:280px;left:0;width:100%;height:178px;background:var(--blue)}
  .mission-text{padding:14px 10px 0;font-family:"Roboto Condensed",sans-serif;font-size:16px;line-height:1.5;color:var(--white);text-align:center;white-space:nowrap}
  .cta{position:absolute;top:434px;left:32px;width:336px;height:40px;background:var(--orange);color:var(--white);font-family:"Oswald",sans-serif;font-size:22px;line-height:40px;text-align:center;box-shadow:0 3px 4px rgba(0,0,0,.25);z-index:3}

  .photo{position:absolute;top:458px;left:0;width:100%;height:502px;background:linear-gradient(180deg,#e4e5e7 0%,#eeeff1 38%,#dfe3e8 58%,#f4f5f7 75%,#e2e6eb 100%)}

  .stats{position:absolute;top:486px;left:0;width:100%;display:flex;justify-content:center;z-index:2}
  .stat{width:118px;display:flex;flex-direction:column;align-items:center;text-align:center;color:var(--blue)}
  .stat + .stat{border-left:1.5px solid var(--orange)}
  .stat-icon{width:78px;height:78px}
  .stat-value{margin-top:6px;font-weight:700;font-size:20px;line-height:1.1}
  .stat-label{font-weight:600;font-size:10.5px;line-height:1.35}

  .url-band{position:absolute;left:0;top:878px;width:262px;height:52px;background:var(--navy);clip-path:polygon(0 0,100% 0,90% 100%,0 100%);z-index:2}
  .url{position:absolute;left:0;top:878px;width:232px;height:52px;line-height:52px;text-align:center;color:var(--white);font-weight:700;font-size:19px;z-index:3}
  .edge-tab{position:absolute;right:0;top:862px;width:18px;height:68px;background:var(--blue-light);clip-path:polygon(60% 0,100% 0,100% 100%,0 100%);z-index:2}
</style>
</head>
<body>
  <main class="banner">
    <header class="brand">
      <span class="brand-mark"></span>
      <div class="brand-text">
        <span class="brand-name">TRVA</span>
        <span class="brand-full">Crossward Surgical Results Alliance</span>
      </div>
    </header>

    <h1 class="headline">50 HOSPITALS ACROSS<br><span class="accent-green">18 STATES</span><br>AND <span class="accent-blue">2 COUNTRIES</span></h1>

    <section class="mission">
      <p class="mission-text">We are a group of passionate individuals working<br>together to improve care for patients undergoing<br>surgery.&nbsp; Our members include clinicians, quality<br>improvement experts, software developers,<br>statisticians, researchers, and administrators.</p>
    </section>
    <div class="cta">PLEASE JOIN US ON OUR MISSION</div>

    <div class="photo" role="img" aria-label="Photo of a clinician's hands typing on a white keyboard in a bright medical office"></div>

    <section class="stats">
      <div class="stat">
        <svg class="stat-icon" viewBox="0 0 80 80" aria-hidden="true">
          <circle cx="40" cy="40" r="38" fill="var(--orange)"/>
          <circle cx="40" cy="40" r="34" fill="none" stroke="#fff" stroke-width="1.5"/>
          <rect x="27" y="22" width="26" height="35" rx="2" fill="#fff"/>
          <rect x="34" y="19" width="12" height="6" rx="1.5" fill="var(--orange-dark)"/>
          <g stroke="var(--orange)" stroke-width="2.4">
            <line x1="31" y1="32" x2="34" y2="32"/><line x1="37" y1="32" x2="49" y2="32"/>
            <line x1="31" y1="40" x2="34" y2="40"/><line x1="37" y1="40" x2="49" y2="40"/>
            <line x1="31" y1="48" x2="34" y2="48"/><line x1="37" y1="48" x2="49" y2="48"/>
          </g>
        </svg>
        <div class="stat-value">9</div>
        <div class="stat-label">MILLION<br>CASES</div>
      </div>
      <div class="stat">
        <svg class="stat-icon" viewBox="0 0 80 80" aria-hidden="true">
          <circle cx="40" cy="40" r="38" fill="var(--orange)"/>
          <circle cx="40" cy="40" r="34" fill="none" stroke="#fff" stroke-width="1.5"/>
          <g transform="rotate(-45 40 40)" fill="#fff">
            <rect x="33" y="26" width="14" height="26" rx="1"/>
            <rect x="30" y="24" width="20" height="3"/>
            <rect x="38.5" y="14" width="3" height="10"/>
            <rect x="34" y="12" width="12" height="3"/>
            <rect x="39.3" y="52" width="1.4" height="14"/>
          </g>
          <g transform="rotate(-45 40 40)" stroke="var(--orange)" stroke-width="1.5">
            <line x1="36" y1="32" x2="41" y2="32"/><line x1="36" y1="38" x2="41" y2="38"/><line x1="36" y1="44" x2="41" y2="44"/>
          </g>
        </svg>
        <div class="stat-value">123</div>
        <div class="stat-label">MILLION<br>MEDICATION<br>RECORDS</div>
      </div>
      <div class="stat">
        <svg class="stat-icon" viewBox="0 0 80 80" aria-hidden="true">
          <circle cx="40" cy="40" r="38" fill="var(--orange)"/>
          <circle cx="40" cy="40" r="34" fill="none" stroke="#fff" stroke-width="1.5"/>
          <path d="M40 58 C22 46 18 38 18 31 C18 24 23 20 29 20 C34 20 38 23 40 27 C42 23 46 20 51 20 C57 20 62 24 62 31 C62 38 58 46 40 58 Z" fill="#fff"/>
          <polyline points="21,39 32,39 35,33 39,46 43,29 46,39 59,39" fill="none" stroke="var(--orange)" stroke-width="2.2" stroke-linejoin="round"/>
        </svg>
        <div class="stat-value">18</div>
        <div class="stat-label">BILLION<br>PHYSIOLOGIC<br>OBSERVATIONS</div>
      </div>
    </section>

    <div class="url-band"></div>
    <div class="url">www.trva-net.org</div>
    <div class="edge-tab"></div>
  </main>
</body>
</html>
```